A5 front cover for a programme DANCE

To design a front cover for our dance Academy 15th Year anniversary show. The theme is movies and musicals

the school is called Bramblewood Academy of Dance and Performing Arts

venue Halvick Playhouse

a5 fornt cover
date 30th June 2019

show title Ride the tides

Number of Pages Required

1 page

Font styles to use
Sans Serif

Colors

Designer to choose colors to be used in the design.

Requirements
Must have
• up to date fun

```html
<!DOCTYPE html>
<html lang="en">
<head>
<meta charset="utf-8">
<title>Ride the Tides – Programme Cover</title>
<link rel="stylesheet" href="https://fonts.googleapis.com/css2?family=Bungee+Inline&family=Cinzel:wght@400;600&display=swap">
<style>
  :root {
    --ink: #05070d;
    --night: #0b1020;
    --glow-red: #b3203a;
    --glow-blue: #3a6fd0;
    --anniversary-red: #c8141a;
    --title-white: #ffffff;
    --title-orange: #ffa200;
    --the-orange: #ff5a14;
    --date-white: #ffffff;
    --venue-orange: #ffa200;
    --muted: #b9bcc4;
    --brand-red: #d0121b;
  }
  * { margin: 0; padding: 0; box-sizing: border-box; }
  html, body {
    width: 834px; height: 1200px; overflow: hidden;
    background: var(--ink);
  }
  .cover {
    position: relative;
    width: 834px; height: 1200px;
    overflow: hidden;
    background: var(--ink);
    font-family: "Cinzel", serif;
    text-align: center;
  }
  .backdrop {
    position: absolute; inset: 0;
    background:
      radial-gradient(circle at 82% 44%, rgba(230,70,60,.55) 0, rgba(179,32,58,.35) 16%, transparent 38%),
      radial-gradient(circle at 62% 18%, rgba(90,150,255,.45) 0, rgba(58,111,208,.18) 14%, transparent 30%),
      radial-gradient(circle at 12% 60%, rgba(140,120,60,.25) 0, transparent 22%),
      radial-gradient(ellipse at 50% 40%, #1a1c2c 0, var(--night) 45%, var(--ink) 85%);
  }
  .mirror-ball {
    position: absolute;
    left: 136px; top: 108px;
    width: 570px; height: 570px;
    border-radius: 50%;
    background:
      radial-gradient(circle at 60% 22%, rgba(255,255,255,.75) 0, rgba(200,205,220,.35) 18%, transparent 42%),
      radial-gradient(circle at 50% 50%, #6b6e78 0, #3a3c46 45%, #15161d 72%, rgba(10,10,16,0) 100%);
    opacity: .9;
  }
  .anniversary {
    position: absolute; left: 0; right: 0; top: 56px;
    color: var(--anniversary-red);
    font-size: 41px; font-weight: 400;
    letter-spacing: 1px;
  }
  .show-title {
    position: absolute; left: 0; top: 0;
    width: 834px; height: 600px;
  }
  .show-title text { font-family: "Bungee Inline", sans-serif; }
  .date {
    position: absolute; left: 0; right: 0; top: 690px;
    color: var(--date-white);
    font-size: 60px; font-weight: 600;
  }
  .venue {
    position: absolute; left: 0; right: 0; top: 772px;
    color: var(--venue-orange);
    font-size: 36px; font-weight: 600;
  }
  .organiser-label {
    position: absolute; left: 0; right: 0; top: 880px;
    color: var(--muted);
    font-size: 18px; letter-spacing: 8px;
  }
  .academy {
    position: absolute; left: 0; right: 0; top: 960px;
    color: var(--brand-red);
    font-weight: 600;
  }
  .academy-name { display: block; font-size: 66px; line-height: 1.1; }
  .academy-tagline { display: block; font-size: 20px; letter-spacing: 1px; margin-top: 14px; }
</style>
</head>
<body>
  <main class="cover">
    <div class="backdrop" role="img" aria-label="Dark stage background with blurred red and blue spotlight bokeh"></div>
    <div class="mirror-ball" role="img" aria-label="Spiked silver mirror ball photograph glowing under stage lights"></div>

    <p class="anniversary">15th Year Anniversary</p>

    <svg class="show-title" viewBox="0 0 834 600" aria-label="Ride the Tides">
      <text x="140" y="386" font-size="190" fill="var(--title-white)" textLength="455" lengthAdjust="spacingAndGlyphs">RIDE</text>
      <text transform="translate(620 213) rotate(90)" x="0" y="0" font-size="88" fill="var(--the-orange)" textLength="169" lengthAdjust="spacingAndGlyphs">THE</text>
      <text x="140" y="569" font-size="168" fill="var(--title-orange)" textLength="557" lengthAdjust="spacingAndGlyphs">TIDES</text>
    </svg>

    <p class="date">30th June 2019</p>
    <p class="venue">Halvick Playhouse</p>

    <p class="organiser-label">ORGANISED BY</p>
    <p class="academy">
      <span class="academy-name">Bramblewood</span>
      <span class="academy-tagline">ACADEMY OF DANCE AND PERFORMING ARTS</span>
    </p>
  </main>
</body>
</html>
```